Professional Coaching Business Letterhead/Footer

I need a letterhead and email footer for my personal coaching business, Dorian K Falstead Professional Coaching. I send several attachments to new clients (such as welcome letter, fee structure, etc) and would like these pages to have my branding on them.
I prefer the black and gold/silver color scheme, and will attach my logo to be used. I'd like the overall impression to be upmarket/regal/professional.

One of the uploaded files is my business card, to give an idea of the style/feel I like. The others are vector files containing logo to be used.

Target Market(s)

Corporate managers, successful business people. 30-60 yrs old.

Industry/Entity Type

Business

Requirements
Must have
• Logo (DKF)
Nice to have
• Shield emblem around logo, some type of watermark.
Should not have
• The first uploaded file is my business card, intended to show style and colors- not to be used itself as the letterhead.

```html
<!DOCTYPE html>
<html lang="en">
<head>
<meta charset="utf-8">
<title>Dorian K Falstead Professional Coaching – Letterhead</title>
<link rel="stylesheet" href="https://fonts.googleapis.com/css2?family=Oswald:wght@500;600&display=swap">
<style>
  :root {
    --backdrop: #ffffff;
    --sheet: #121212;
    --sheet-edge: #050505;
    --sheet-glow: rgba(150, 150, 130, 0.35);
    --silver: #c9c9c9;
    --silver-dim: #6d6d6d;
    --gold: #f0a91e;
    --white: #f4f4f4;
  }
  html, body {
    margin: 0;
    padding: 0;
    width: 1200px;
    height: 1000px;
    overflow: hidden;
    background: var(--backdrop);
  }
  .canvas {
    position: relative;
    width: 1200px;
    height: 1000px;
    font-family: "Oswald", "Arial Narrow", sans-serif;
  }
  .letterhead {
    position: absolute;
    left: 224px;
    top: 15px;
    width: 752px;
    height: 971px;
    box-sizing: border-box;
    border: 3px solid var(--sheet-edge);
    border-radius: 6px;
    background:
      radial-gradient(circle at 120px 95px, var(--sheet-glow) 0, rgba(0,0,0,0) 110px),
      radial-gradient(ellipse at 50% 45%, #1a1a1a 0, var(--sheet) 60%, #0a0a0a 100%);
    overflow: hidden;
  }
  .brand {
    position: absolute;
    left: 50px;
    top: 58px;
    width: 140px;
    text-align: center;
  }
  .brand-mark {
    display: block;
    margin: 0 auto;
  }
  .brand-name {
    margin-top: 6px;
    font-weight: 500;
    font-size: 12px;
    letter-spacing: 0.5px;
    color: var(--silver);
    white-space: nowrap;
  }
  .footer {
    position: absolute;
    left: 0;
    right: 0;
    bottom: 0;
    height: 60px;
  }
  .footer-service,
  .footer-phone {
    position: absolute;
    top: 16px;
    font-weight: 600;
    font-size: 24px;
    line-height: 1;
    white-space: nowrap;
    transform-origin: left top;
  }
  .footer-service {
    left: 24px;
    color: var(--gold);
    transform: scaleX(0.58);
  }
  .footer-divider {
    position: absolute;
    left: 180px;
    top: 17px;
    width: 2px;
    height: 35px;
    background: var(--white);
  }
  .footer-phone {
    left: 192px;
    color: var(--white);
    transform: scaleX(0.6);
  }
  .footer-contact {
    position: absolute;
    right: 32px;
    top: 15px;
    text-align: right;
    font-weight: 600;
    font-size: 15px;
    line-height: 20px;
    color: var(--gold);
    transform: scaleX(0.74);
    transform-origin: right top;
    white-space: nowrap;
  }
  .footer-contact div { margin: 0; }
</style>
</head>
<body>
<main class="canvas">
  <section class="letterhead" aria-label="Letterhead page">
    <header class="brand">
      <svg class="brand-mark" width="86" height="86" viewBox="0 0 86 86" aria-hidden="true">
        <circle cx="43" cy="43" r="40" fill="none" stroke="var(--silver-dim)" stroke-width="4"/>
      </svg>
      <div class="brand-name">DORIAN K FALSTEAD</div>
    </header>

    <footer class="footer">
      <div class="footer-service">PROFESSIONAL COACHING</div>
      <div class="footer-divider"></div>
      <div class="footer-phone">PHONE : 503.555.0147</div>
      <div class="footer-contact">
        <div>DORIANFALSTEAD.COM</div>
        <div>dorian@DORIANFALSTEAD.COM</div>
      </div>
    </footer>
  </section>
</main>
</body>
</html>
```